TORVEL Business Card Design

We need a business card design for a current Plastering company now moving to building and constructing new homes.
We have been in the Plastering(rendering) business for 15yrs and have made a good name with our customers for our Top Quality of work that we provide.
We would like TORVEL to be the main attraction with an image of architectural roof tops or house design within it. Blue Yellow and Black are colours we like but are willing to see other ideas.
We would like the design to be modern and communicate quality and experience.
Industry/Entity Type
Building
Contact Information for Business Card
TORVEL Building and Plastering
PO BOX 57390 Marlowe Darwin NT 0815
PH/Fax: 08 89317725 Email: torvel@quellnet.com
Dale: 0417396248 Rosa:0409273516
ABN:58 297 130 846

```html
<!DOCTYPE html>
<html lang="en">
<head>
<meta charset="utf-8">
<title>TORVEL Business Card</title>
<link rel="stylesheet" href="https://fonts.googleapis.com/css2?family=Open+Sans:wght@400;600;700&display=swap">
<style>
  :root {
    --page-bg: #3a2a1f;
    --sun-top: #dde125;
    --sun-bottom: #f5b01b;
    --road: #2a2a2a;
    --roofs: #3a3a3a;
    --card-white: #ffffff;
    --ink: #4a4a4a;
    --ink-dark: #1e1e1e;
    --back-black: #000000;
    --back-glow: #2b2b2b;
    --accent-yellow: #e8c61c;
    --text-light: #ffffff;
    --text-muted: #c9c9c9;
  }
  * { box-sizing: border-box; margin: 0; padding: 0; }
  html, body { width: 1200px; height: 1000px; overflow: hidden; }
  body {
    background: var(--page-bg);
    font-family: "Open Sans", Arial, sans-serif;
    position: relative;
  }
  .card {
    position: absolute;
    left: 360px;
    width: 481px;
    height: 297px;
    overflow: hidden;
    box-shadow: 0 4px 14px rgba(0,0,0,.5);
  }
  /* Front */
  .card-front { top: 135px; background: var(--card-white); }
  .sky-band {
    position: absolute; left: 0; top: 0; width: 100%; height: 82px;
    background: linear-gradient(to bottom, var(--sun-top), var(--sun-bottom));
  }
  .street-band {
    position: absolute; left: 0; top: 82px; width: 100%; height: 33px;
    background: var(--road);
  }
  .fold-shadow {
    position: absolute; left: 0; top: 115px; width: 100%; height: 16px;
    background: linear-gradient(to bottom, #c9c9c9, #ffffff);
  }
  .rooftops-art {
    position: absolute; left: 148px; top: 16px; width: 182px; height: 99px;
    background: linear-gradient(to bottom, #454545, var(--roofs));
  }
  .brand {
    position: absolute; left: 50px; top: 150px; width: 382px;
    display: flex; align-items: center; justify-content: flex-end; gap: 18px;
  }
  .brand-dot {
    width: 46px; height: 46px; border-radius: 50%; background: var(--ink-dark);
  }
  .brand-name {
    font-weight: 400; font-size: 80px; line-height: 1; color: var(--ink);
    letter-spacing: 1px;
  }
  .tagline {
    position: absolute; right: 50px; top: 240px; text-align: right; color: var(--ink-dark);
  }
  .tagline-main { font-size: 13px; font-weight: 700; line-height: 16px; }
  .tagline-sub { font-size: 10.5px; line-height: 14px; }
  .tagline-sub strong { font-size: 12px; }
  /* Back */
  .card-back {
    top: 568px;
    background: radial-gradient(ellipse 220px 200px at 260px 150px, var(--back-glow), var(--back-black));
  }
  .skyline-art {
    position: absolute; left: 50px; top: 28px; width: 330px; height: 50px;
    background: linear-gradient(to top, var(--accent-yellow), rgba(232,198,28,0.15));
    opacity: .85;
  }
  .horizon {
    position: absolute; left: 5px; top: 78px; width: 470px; height: 1px;
    background: linear-gradient(to right, transparent, #8a8a8a 20%, #8a8a8a 80%, transparent);
  }
  .contact {
    position: absolute; right: 54px; top: 130px; text-align: right;
    color: var(--text-muted); font-size: 11px; line-height: 15.2px; font-weight: 600;
  }
  .contact h2 {
    color: var(--text-light); font-size: 17px; font-weight: 700; line-height: 22px;
  }
  .contact .name { color: var(--text-light); font-weight: 700; }
</style>
</head>
<body>
  <section class="card card-front">
    <div class="sky-band"></div>
    <div class="street-band"></div>
    <div class="fold-shadow"></div>
    <div class="rooftops-art" role="img" aria-label="Illustration of three dark houses with pitched roofs on the street line"></div>
    <div class="brand">
      <span class="brand-dot"></span>
      <span class="brand-name">TORVEL</span>
    </div>
    <div class="tagline">
      <p class="tagline-main">building and plastering</p>
      <p class="tagline-sub">more than <strong>15</strong> years of experience</p>
    </div>
  </section>

  <section class="card card-back">
    <div class="skyline-art" role="img" aria-label="Yellow city skyline silhouette reflected on a horizon line"></div>
    <div class="horizon"></div>
    <div class="contact">
      <h2>CONTACT INFORMATION</h2>
      <p>TORVEL Building and Plastering PO BOX 57390 Marlowe Darwin NT 0815</p>
      <p>PH/Fax: 08 89317725</p>
      <p>Contact personally:</p>
      <p><span class="name">Dale</span> - torvel@quellnet.com</p>
      <p>0417396248</p>
      <p><span class="name">Rosa</span> - 0409273516</p>
      <p>ABN:58 297 130 846</p>
    </div>
  </section>
</body>
</html>
```